Weightloss company needs Business Card

We want a business card that is clean and professional, yet portrays that we are a friendly, innovative, and versatile program designed to fit the needs of our clients.
I would like there to be 2 sides, one side having an appointment card, and the other side containing the logo and business information. There can be decorations on both sides. The logo is attached.

Target Market(s)

Men and women 40-60

Industry/Entity Type

Business

Contact Information for Business Card

Font styles to use
Sans Serif

Requirements
Must have
• The logo, space for business information
Nice to have
• The colors in the logo
Should not have
• No pictures of people or food

```html
<!DOCTYPE html>
<html lang="en">
<head>
<meta charset="utf-8">
<title>Renewa Wellness – Business Card</title>
<link href="https://fonts.googleapis.com/css2?family=Exo+2:ital,wght@0,400;0,500;0,700;1,500&display=swap" rel="stylesheet">
<style>
  :root {
    --bg: #b9babd;
    --red: #e10a17;
    --red-deep: #a50f10;
    --blue: #2aa8e0;
    --white: #ffffff;
    --grey-text: #8a8a8a;
    --line: #9a9a9a;
  }
  * { margin: 0; padding: 0; box-sizing: border-box; }
  html, body { width: 1200px; height: 1200px; overflow: hidden; }
  body {
    background: var(--bg);
    font-family: "Exo 2", Arial, sans-serif;
    display: flex;
    flex-direction: column;
    align-items: center;
    justify-content: center;
    gap: 56px;
  }
  .card {
    position: relative;
    width: 900px;
    height: 514px;
    background: var(--white);
    overflow: hidden;
    box-shadow: 0 10px 28px rgba(0,0,0,0.22);
  }
  .card__shapes { position: absolute; inset: 0; width: 100%; height: 100%; }

  /* Appointment side */
  .address {
    position: absolute; left: 36px; top: 52px;
    color: var(--white); font-weight: 500; font-size: 24px; line-height: 1.35;
  }
  .appointments {
    position: absolute; right: 60px; top: 120px;
    color: var(--red); font-weight: 700; font-style: italic; font-size: 46px;
  }
  .slots { position: absolute; left: 420px; right: 60px; top: 215px; }
  .slot {
    display: flex; align-items: flex-end; gap: 10px;
    color: var(--grey-text); font-size: 26px; font-style: italic;
    margin-bottom: 26px;
  }
  .slot__rule { flex: 1; border-bottom: 2px solid var(--line); margin-bottom: 6px; }

  /* Logo side */
  .brand {
    position: absolute; left: 300px; right: 60px; top: 150px;
    text-align: center;
  }
  .brand__name {
    color: var(--red); font-weight: 700; font-size: 66px; line-height: 1.05;
  }
  .phones {
    position: absolute; left: 40px; bottom: 56px;
    color: var(--white); font-size: 36px; font-weight: 500;
  }
  .contact-row { display: flex; align-items: center; gap: 14px; line-height: 1.3; }
  .contact-row svg { width: 28px; height: 28px; fill: currentColor; }
  .web {
    position: absolute; right: 46px; bottom: 40px;
    color: var(--grey-text); font-size: 34px; font-weight: 500; text-align: right;
  }
  .web .contact-row { justify-content: flex-end; }
  .web svg { fill: var(--red); }
</style>
</head>
<body>

  <section class="card card--appointment">
    <svg class="card__shapes" viewBox="0 0 900 514" preserveAspectRatio="none" aria-hidden="true">
      <defs>
        <linearGradient id="redFade" x1="0" y1="0" x2="0" y2="1">
          <stop offset="0" stop-color="#e10a17"/>
          <stop offset="1" stop-color="#a50f10"/>
        </linearGradient>
      </defs>
      <rect width="900" height="514" fill="url(#redFade)"/>
      <polygon points="500,0 900,0 900,514 380,514 318,58" fill="#2aa8e0"/>
      <polygon points="520,10 900,10 900,514 392,514 332,66" fill="#ffffff"/>
    </svg>
    <p class="address">Dummy City<br>Dummy Country Land</p>
    <h2 class="appointments">Appointments</h2>
    <div class="slots">
      <div class="slot"><span>Date.</span><span class="slot__rule"></span></div>
      <div class="slot"><span>Time.</span><span class="slot__rule"></span></div>
      <div class="slot"><span>Date.</span><span class="slot__rule"></span></div>
      <div class="slot"><span>Time.</span><span class="slot__rule"></span></div>
    </div>
  </section>

  <section class="card card--brand">
    <svg class="card__shapes" viewBox="0 0 900 514" preserveAspectRatio="none" aria-hidden="true">
      <defs>
        <linearGradient id="redFade2" x1="0" y1="0" x2="0" y2="1">
          <stop offset="0" stop-color="#e10a17"/>
          <stop offset="1" stop-color="#a50f10"/>
        </linearGradient>
      </defs>
      <rect width="900" height="514" fill="url(#redFade2)"/>
      <polygon points="250,0 900,0 900,514 400,514 130,170" fill="#2aa8e0"/>
      <polygon points="268,8 900,8 900,514 418,514 146,172" fill="#ffffff"/>
    </svg>
    <div class="brand">
      <span class="brand__name">Renewa<br>Wellness</span>
    </div>
    <div class="phones">
      <div class="contact-row">
        <svg viewBox="0 0 24 24"><path d="M6 2h4l2 5-2.5 1.5a11 11 0 0 0 6 6L17 12l5 2v4a2 2 0 0 1-2 2A18 18 0 0 1 4 4a2 2 0 0 1 2-2z"/></svg>
        <span>111.222.3333</span>
      </div>
      <div class="contact-row">
        <svg viewBox="0 0 24 24"><path d="M6 2h12v6H6zM3 9h18a1 1 0 0 1 1 1v7h-4v5H6v-5H2v-7a1 1 0 0 1 1-1zm5 8v3h8v-3z"/></svg>
        <span>111.222.3333</span>
      </div>
    </div>
    <div class="web">
      <div class="contact-row">
        <span>www.renewawell.com</span>
        <svg viewBox="0 0 24 24"><path d="M12 2a10 10 0 1 0 0 20 10 10 0 0 0 0-20zm0 2c1 1.3 1.8 3 2.1 5H9.9C10.2 7 11 5.3 12 4zM4.3 11h3.6a15 15 0 0 0 0 2H4.3a8 8 0 0 1 0-2zm5.6 0h4.2a13 13 0 0 1 0 2H9.9a13 13 0 0 1 0-2zm6.2 0h3.6a8 8 0 0 1 0 2h-3.6a15 15 0 0 0 0-2zM9.9 15h4.2c-.3 2-1.1 3.7-2.1 5-1-1.3-1.8-3-2.1-5z"/></svg>
      </div>
      <div class="contact-row">
        <span>info@renewawell.com</span>
        <svg viewBox="0 0 24 24"><path d="M2 5h20v14H2zm2 2v.5l8 5 8-5V7z"/></svg>
      </div>
    </div>
  </section>

</body>
</html>
```